Gold Harbor Concierge

I need a website developed for our travel concierge service. I'm looking to be able to collect information and have the information collected directed to a inbox. I would also like to me able to manage the updates to the website myself. I also would like a mobile version of the website to be included. Our services include assistance with Bachelor Parties, Bachelorette Parties and Medical Tourism. We provide custom packages that include Airport Transportation, Lodging, Bilingual guides and any other special needs identified by our clients.
Industry/Entity Type
Travel
Coding
Coded - Design and coding required
Number of Pages Required
4 page
Look and feel

```html
<!DOCTYPE html>
<html lang="en">
<head>
<meta charset="utf-8">
<title>Gold Harbor Concierge – Destination Pages</title>
<link href="https://fonts.googleapis.com/css2?family=Libre+Baskerville:wght@400;700&family=Oswald:wght@400;500&family=Open+Sans:wght@400;600&display=swap" rel="stylesheet">
<style>
:root{
  --gold:#d59d36;
  --gold-deep:#c08a2a;
  --black:#000;
  --ink:#1a1a1a;
  --white:#fff;
  --line:#9a9a9a;
  --sheet:#ffffff;
}
*{box-sizing:border-box;margin:0;padding:0}
html,body{width:864px;height:1200px;overflow:hidden;background:var(--sheet)}
body{position:relative;font-family:"Open Sans",sans-serif}

.page{position:absolute;top:14.8px;width:767px;height:2211px;transform:scale(.5288);transform-origin:0 0;overflow:hidden;background:var(--black)}
.page--sosua{left:18.5px}
.page--mexico{left:440.5px}
.abs{position:absolute}

/* hero */
.hero-photo{position:absolute;left:0;top:0;width:767px;height:310px;background:radial-gradient(ellipse at 30% 60%,#5a3d3a 0%,#2d1f2c 40%,#120b16 80%),#120b16}
.hero-photo::after{content:"";position:absolute;inset:0;background:linear-gradient(180deg,rgba(0,0,0,.55),rgba(40,20,60,.25) 60%,rgba(0,0,0,.3))}
.hero-curve{position:absolute;left:0;top:0}
.contact{position:absolute;top:13px;display:flex;align-items:center;gap:8px;font-weight:600;font-size:11px;color:var(--gold)}
.contact--mail{left:110px}
.contact--phone{right:112px}
.contact-icon{width:20px;height:20px;border-radius:50%;background:var(--gold);display:flex;align-items:center;justify-content:center}
.nav{position:absolute;top:50px;font-family:"Oswald",sans-serif;font-size:13px;color:var(--gold);text-transform:uppercase}
.brand{position:absolute;left:283px;top:10px;width:200px;text-align:center;color:var(--gold);font-family:"Libre Baskerville",serif}
.brand-ring{width:40px;height:40px;margin:0 auto 6px;border:2px solid var(--gold);border-radius:50%}
.brand-name{font-size:17px;line-height:1}
.brand-sub{font-size:5.5px;letter-spacing:4px;margin-top:5px}
.hero-title{position:absolute;left:0;width:767px;top:158px;text-align:center;font-family:"Libre Baskerville",serif;font-weight:700;font-size:28px;color:var(--gold)}

/* intro */
.section-title{position:absolute;left:0;width:767px;text-align:center;font-family:"Libre Baskerville",serif;font-weight:700;font-size:17px;line-height:24px;letter-spacing:.5px;color:var(--gold);text-transform:uppercase}
.intro-title{top:358px}
.feature-card{position:absolute;width:257px;height:201px;border:2px solid var(--gold);border-radius:18px;overflow:hidden;background:var(--black)}
.feature-photo{position:absolute;left:0;top:0;width:100%;height:156px}
.feature-label{position:absolute;bottom:9px;font-family:"Libre Baskerville",serif;font-weight:700;font-size:16px;letter-spacing:1px;color:var(--gold)}
.feature-copy{position:absolute;width:267px;font-size:7.4px;line-height:15.3px;color:var(--white);text-align:justify}
.feature-copy p+p{margin-top:7px}

/* form */
.quote{position:absolute;left:0;top:932px;width:767px;height:596px;background:var(--white);color:var(--ink)}
.quote-title{position:absolute;left:0;width:767px;text-align:center;font-family:"Libre Baskerville",serif;font-weight:700;font-size:18px;line-height:22px}
.quote-title .accent{color:var(--gold);display:block}
.label{position:absolute;font-size:8.5px;color:var(--ink)}
.label b{color:#d2261c;font-weight:400}
.choices{position:absolute;display:flex;gap:9px;font-size:7.5px}
.choice{display:flex;align-items:center;gap:4px}
.radio{width:9px;height:9px;border:1px solid #222;border-radius:50%}
.field{position:absolute;height:24px;border:1px solid #666;border-radius:2px;font-size:7px;color:#444;padding:6px 5px}
.field--date::after{content:"";position:absolute;right:6px;top:7px;width:8px;height:8px;border:1px solid #444;border-top-width:2px}
.checks{position:absolute;display:flex;flex-direction:column;gap:12.6px;font-size:7px;color:#333}
.check{display:flex;align-items:flex-start;gap:6px;line-height:9px}
.box{flex:none;width:8px;height:8px;border:1px solid #555;border-radius:1px}
.send{position:absolute;left:478px;top:519px;width:97px;height:24px;background:var(--gold);border-radius:2px;color:var(--white);font-size:8px;font-weight:600;text-align:center;line-height:24px}

/* activities */
.activities{position:absolute;left:0;top:1528px;width:767px;height:359px;background:radial-gradient(ellipse at 50% 60%,#e0ad4c,#cf9a33 70%,#c8922d)}
.activities .section-title{color:var(--white);top:44px;font-size:17px;line-height:22px}
.activity{position:absolute;top:128px;width:129px;text-align:center}
.activity-photo{width:129px;height:106px;border-radius:4px 16px 16px 4px}
.activity-name{margin-top:11px;font-family:"Oswald",sans-serif;font-size:13.5px;color:var(--white);text-transform:uppercase}
.dots{position:absolute;top:297px;left:358px;display:flex;gap:8px}
.dot{width:9px;height:9px;border-radius:50%;background:#a77a26}
.dot--on{background:var(--black)}

/* footer */
.footer{position:absolute;left:0;top:1887px;width:767px;height:324px;background:var(--black)}
.footer .brand{top:38px}
.footer .brand-ring{width:84px;height:84px;margin-bottom:14px}
.footer .brand-name{font-size:30px}
.footer .brand-sub{font-size:8px;letter-spacing:7px;margin-top:8px}
.social{position:absolute;top:203px;left:270px;display:flex;gap:7px}
.social-item{width:32px;height:32px;border-radius:50%;background:var(--gold)}
.rule{position:absolute;left:110px;top:272px;width:545px;height:1px;background:#555}
.copyright{position:absolute;left:0;width:767px;top:293px;text-align:center;font-size:9.5px;color:var(--white)}
</style>
</head>
<body>

<!-- Sosua destination page -->
<section class="page page--sosua">
  <div class="hero-photo" role="img" aria-label="Photo of a group of men cheering at a nightclub"></div>
  <svg class="hero-curve" width="767" height="320" viewBox="0 0 767 320" aria-hidden="true">
    <path d="M0 245 Q383.5 360 767 245 L767 320 L0 320 Z" fill="#000"/>
    <path d="M0 245 Q383.5 360 767 245" fill="none" stroke="#d59d36" stroke-width="4"/>
  </svg>
  <div class="contact contact--mail"><span class="contact-icon"><svg width="10" height="8" viewBox="0 0 10 8"><rect x=".5" y=".5" width="9" height="7" fill="none" stroke="#000"/><path d="M.5 .5 5 4.5 9.5 .5" fill="none" stroke="#000"/></svg></span>MAIL: hello@goldharbor.example</div>
  <div class="contact contact--phone"><span class="contact-icon"><svg width="10" height="10" viewBox="0 0 10 10"><path d="M2 1 L4 3 L3 4.3 Q4.5 6 5.7 7 L7 6 L9 8 L7.8 9.3 Q3 8.5 .7 2.2Z" fill="#000"/></svg></span>TOLL-FREE: +1 800 555 0142</div>
  <div class="nav" style="left:108px">Home</div>
  <div class="nav" style="left:161px">Destinations</div>
  <div class="nav" style="left:250px">About Us</div>
  <div class="nav" style="left:465px">Services</div>
  <div class="nav" style="left:531px">Nightlife</div>
  <div class="nav" style="left:603px">Contact Us</div>
  <div class="brand"><div class="brand-ring"></div><div class="brand-name">Gold Harbor</div><div class="brand-sub">CONCIERGE</div></div>
  <h1 class="hero-title">SOSUA</h1>

  <h2 class="section-title intro-title">Custom<br>Sosua Bachelor Party Packages</h2>
  <div class="feature-card" style="left:110px;top:444px">
    <div class="feature-photo" role="img" aria-label="Photo of friends laughing together at a bar" style="background:linear-gradient(135deg,#6b4a3a,#a07260 45%,#4b3a38)"></div>
    <div class="feature-label" style="right:10px">PARTY DANCE</div>
  </div>
  <div class="feature-copy" style="left:388px;top:450px">
    <p>Our hosts plan every detail of your weekend, from airport pickup to late tables, so the group can relax, celebrate and enjoy the coast. Each package is shaped around your dates, budget and the pace your crew prefers for the trip. Bilingual guides, private drivers and trusted venues are arranged ahead of time, and one coordinator stays on call from arrival until the last ride back to the airport.</p>
    <p>Tell us the group size and the nights you want to go out, and we will return a clear plan with venues, timing and transport for every stop. Prices are confirmed before you book.</p>
  </div>
  <div class="feature-copy" style="left:110px;top:678px">
    <p>Our hosts plan every detail of your weekend, from airport pickup to late tables, so the group can relax, celebrate and enjoy the coast. Each package is shaped around your dates, budget and the pace your crew prefers for the trip. Bilingual guides, private drivers and trusted venues are arranged ahead of time, and one coordinator stays on call from arrival until the last ride back to the airport.</p>
    <p>Tell us the group size and the nights you want to go out, and we will return a clear plan with venues, timing and transport for every stop. Prices are confirmed before you book.</p>
  </div>
  <div class="feature-card" style="left:398px;top:669px">
    <div class="feature-photo" role="img" aria-label="Photo of friends toasting on a beach under palm trees" style="background:linear-gradient(160deg,#5f7a4a,#a8b8a0 45%,#6e5a48)"></div>
    <div class="feature-label" style="left:10px">NIGHT DANCE</div>
  </div>

  <form class="quote">
    <h2 class="quote-title" style="top:52px">FILL THIS OUT NOW<span class="accent">TO GET THE PARTY GOING!</span></h2>
    <div class="label" style="left:110px;top:136px">Party Theme <b>*</b></div>
    <div class="choices" style="left:110px;top:156px"><span class="choice"><i class="radio"></i>Bachelor Party</span><span class="choice"><i class="radio"></i>Birthday Party</span><span class="choice"><i class="radio"></i>Fun Trip</span><span class="choice"><i class="radio"></i>Bachelorette</span></div>
    <div class="label" style="left:407px;top:136px">Group Composition <b>*</b></div>
    <div class="choices" style="left:407px;top:156px"><span class="choice"><i class="radio"></i>All Guys</span><span class="choice"><i class="radio"></i>Mixed</span><span class="choice"><i class="radio"></i>All Girls</span></div>

    <div class="label" style="left:110px;top:188px">Group Size <b>*</b></div>
    <div class="label" style="left:258px;top:188px">Check-in Date <b>*</b></div>
    <div class="label" style="left:368px;top:188px">Check-out Date <b>*</b></div>
    <div class="label" style="left:483px;top:188px">Flexible Dates <b>*</b></div>
    <div class="field" style="left:110px;top:208px;width:135px">Enter approximate number</div>
    <div class="field field--date" style="left:258px;top:208px;width:97px"></div>
    <div class="field field--date" style="left:368px;top:208px;width:97px"></div>
    <div class="choices" style="left:483px;top:215px"><span class="choice"><i class="radio"></i>Yes</span><span class="choice"><i class="radio"></i>No</span></div>

    <div class="label" style="left:110px;top:251px">Choose Your Daytime Activities and Services <b>*</b></div>
    <div class="label" style="left:413px;top:251px">Choose Your Night Time Activities <b>*</b></div>
    <div class="checks" style="left:110px;top:276px"><span class="check"><i class="box"></i>ATV's</span><span class="check"><i class="box"></i>DJ Pool Party</span><span class="check"><i class="box"></i>Golfing</span><span class="check"><i class="box"></i>Private Catamaran Booze Cruise</span><span class="check"><i class="box"></i>Private Deep-Sea Fishing</span><span class="check"><i class="box"></i>Private Chef</span><span class="check"><i class="box"></i>Transportation Services</span></div>
    <div class="checks" style="left:258px;top:276px"><span class="check"><i class="box"></i>Dune Buggies</span><span class="check"><i class="box"></i>Caribbean Beaches</span><span class="check"><i class="box"></i>Private Yacht Booze Cruise</span><span class="check"><i class="box"></i>Shared Catamaran Booze Cruise</span><span class="check"><i class="box"></i>All-Inclusive</span><span class="check"><i class="box"></i>Private Concierge</span></div>
    <div class="checks" style="left:413px;top:276px"><span class="check"><i class="box"></i>VIP Club Party</span><span class="check"><i class="box"></i>Nightlife Tour</span><span class="check"><i class="box"></i>Beach Dinner &amp; Party Warm-Up</span></div>
    <div class="checks" style="left:563px;top:276px;width:100px;gap:11px"><span class="check"><i class="box"></i>Strip and Gent's Clubs Tour</span><span class="check"><i class="box"></i>Casinos Tour</span><span class="check"><i class="box"></i>Beach Bar Crawl</span></div>

    <div class="label" style="left:110px;top:442px">Package Budget Per Person <b>*</b></div>
    <div class="label" style="left:258px;top:442px">First Name <b>*</b></div>
    <div class="label" style="left:368px;top:442px">Last Name <b>*</b></div>
    <div class="label" style="left:478px;top:442px">Email Address <b>*</b></div>
    <div class="field" style="left:110px;top:461px;width:135px">Ex: $500,600$ etc</div>
    <div class="field" style="left:258px;top:461px;width:97px"></div>
    <div class="field" style="left:368px;top:461px;width:97px"></div>
    <div class="field" style="left:478px;top:461px;width:97px"></div>
    <div class="label" style="left:110px;top:500px">Phone Number</div>
    <div class="label" style="left:258px;top:500px">Comments</div>
    <div class="field" style="left:110px;top:519px;width:135px"></div>
    <div class="field" style="left:258px;top:519px;width:207px"></div>
    <div class="send">SEND MY QUOTE</div>
  </form>

  <section class="activities">
    <h2 class="section-title">Bachelor Party<br>Sosua Night Time Activities</h2>
    <div class="activity" style="left:111px"><div class="activity-photo" role="img" aria-label="Photo of friends sharing dinner outdoors" style="background:linear-gradient(135deg,#4a3a30,#8a6a50)"></div><div class="activity-name">VIP Club Party</div></div>
    <div class="activity" style="left:249px"><div class="activity-photo" role="img" aria-label="Photo of a garden dinner under string lights" style="background:linear-gradient(135deg,#2e3a22,#8a7a40)"></div><div class="activity-name">Nightlife Tour</div></div>
    <div class="activity" style="left:388px"><div class="activity-photo" role="img" aria-label="Photo of friends at an outdoor dinner table" style="background:linear-gradient(135deg,#b8b0a0,#7a8a6a)"></div><div class="activity-name">Beach Dinner</div></div>
    <div class="activity" style="left:526px"><div class="activity-photo" role="img" aria-label="Photo of a group at a beach bar table" style="background:linear-gradient(135deg,#6a5a48,#5a8a9a)"></div><div class="activity-name">Beach Bar Crawl</div></div>
    <div class="dots"><i class="dot dot--on"></i><i class="dot"></i><i class="dot"></i></div>
  </section>

  <footer class="footer">
    <div class="brand"><div class="brand-ring"></div><div class="brand-name">Gold Harbor</div><div class="brand-sub">CONCIERGE</div></div>
    <div class="social"><i class="social-item" aria-label="Social link"></i><i class="social-item" aria-label="Social link"></i><i class="social-item" aria-label="Social link"></i><i class="social-item" aria-label="Social link"></i><i class="social-item" aria-label="Social link"></i><i class="social-item" aria-label="Social link"></i></div>
    <div class="rule"></div>
    <div class="copyright">Copyrights @ 2021 Gold Harbor Concierge.</div>
  </footer>
</section>

<!-- Mexico destination page -->
<section class="page page--mexico">
  <div class="hero-photo" role="img" aria-label="Photo of a group of men cheering at a nightclub"></div>
  <svg class="hero-curve" width="767" height="320" viewBox="0 0 767 320" aria-hidden="true">
    <path d="M0 245 Q383.5 360 767 245 L767 320 L0 320 Z" fill="#000"/>
    <path d="M0 245 Q383.5 360 767 245" fill="none" stroke="#d59d36" stroke-width="4"/>
  </svg>
  <div class="contact contact--mail"><span class="contact-icon"><svg width="10" height="8" viewBox="0 0 10 8"><rect x=".5" y=".5" width="9" height="7" fill="none" stroke="#000"/><path d="M.5 .5 5 4.5 9.5 .5" fill="none" stroke="#000"/></svg></span>MAIL: hello@goldharbor.example</div>
  <div class="contact contact--phone"><span class="contact-icon"><svg width="10" height="10" viewBox="0 0 10 10"><path d="M2 1 L4 3 L3 4.3 Q4.5 6 5.7 7 L7 6 L9 8 L7.8 9.3 Q3 8.5 .7 2.2Z" fill="#000"/></svg></span>TOLL-FREE: +1 800 555 0142</div>
  <div class="nav" style="left:108px">Home</div>
  <div class="nav" style="left:161px">Destinations</div>
  <div class="nav" style="left:250px">About Us</div>
  <div class="nav" style="left:465px">Services</div>
  <div class="nav" style="left:531px">Nightlife</div>
  <div class="nav" style="left:603px">Contact Us</div>
  <div class="brand"><div class="brand-ring"></div><div class="brand-name">Gold Harbor</div><div class="brand-sub">CONCIERGE</div></div>
  <h1 class="hero-title">MEXICO</h1>

  <h2 class="section-title intro-title">Custom<br>Mexico Bachelor Party Packages</h2>
  <div class="feature-card" style="left:110px;top:444px">
    <div class="feature-photo" role="img" aria-label="Photo of friends celebrating at an evening party" style="background:linear-gradient(135deg,#3a2a20,#8a6040 50%,#2a1e1a)"></div>
    <div class="feature-label" style="right:10px">PARTY DANCE</div>
  </div>
  <div class="feature-copy" style="left:388px;top:450px">
    <p>Our hosts plan every detail of your weekend, from airport pickup to late tables, so the group can relax, celebrate and enjoy the coast. Each package is shaped around your dates, budget and the pace your crew prefers for the trip. Bilingual guides, private drivers and trusted venues are arranged ahead of time, and one coordinator stays on call from arrival until the last ride back to the airport.</p>
    <p>Tell us the group size and the nights you want to go out, and we will return a clear plan with venues, timing and transport for every stop. Prices are confirmed before you book.</p>
  </div>
  <div class="feature-copy" style="left:110px;top:678px">
    <p>Our hosts plan every detail of your weekend, from airport pickup to late tables, so the group can relax, celebrate and enjoy the coast. Each package is shaped around your dates, budget and the pace your crew prefers for the trip. Bilingual guides, private drivers and trusted venues are arranged ahead of time, and one coordinator stays on call from arrival until the last ride back to the airport.</p>
    <p>Tell us the group size and the nights you want to go out, and we will return a clear plan with venues, timing and transport for every stop. Prices are confirmed before you book.</p>
  </div>
  <div class="feature-card" style="left:398px;top:669px">
    <div class="feature-photo" role="img" aria-label="Photo of friends dining at a table in a field" style="background:linear-gradient(160deg,#7a8a5a,#d8d8c8 45%,#6a6a40)"></div>
    <div class="feature-label" style="left:10px">NIGHT DANCE</div>
  </div>

  <form class="quote">
    <h2 class="quote-title" style="top:52px">FILL THIS OUT NOW<span class="accent">TO GET THE PARTY GOING!</span></h2>
    <div class="label" style="left:110px;top:136px">Party Theme <b>*</b></div>
    <div class="choices" style="left:110px;top:156px"><span class="choice"><i class="radio"></i>Bachelor Party</span><span class="choice"><i class="radio"></i>Birthday Party</span><span class="choice"><i class="radio"></i>Fun Trip</span><span class="choice"><i class="radio"></i>Bachelorette</span></div>
    <div class="label" style="left:407px;top:136px">Group Composition <b>*</b></div>
    <div class="choices" style="left:407px;top:156px"><span class="choice"><i class="radio"></i>All Guys</span><span class="choice"><i class="radio"></i>Mixed</span><span class="choice"><i class="radio"></i>All Girls</span></div>

    <div class="label" style="left:110px;top:188px">Group Size <b>*</b></div>
    <div class="label" style="left:258px;top:188px">Check-in Date <b>*</b></div>
    <div class="label" style="left:368px;top:188px">Check-out Date <b>*</b></div>
    <div class="label" style="left:483px;top:188px">Flexible Dates <b>*</b></div>
    <div class="field" style="left:110px;top:208px;width:135px">Enter approximate number</div>
    <div class="field field--date" style="left:258px;top:208px;width:97px"></div>
    <div class="field field--date" style="left:368px;top:208px;width:97px"></div>
    <div class="choices" style="left:483px;top:215px"><span class="choice"><i class="radio"></i>Yes</span><span class="choice"><i class="radio"></i>No</span></div>

    <div class="label" style="left:110px;top:251px">Choose Your Daytime Activities and Services <b>*</b></div>
    <div class="label" style="left:413px;top:251px">Choose Your Night Time Activities <b>*</b></div>
    <div class="checks" style="left:110px;top:276px"><span class="check"><i class="box"></i>ATV's</span><span class="check"><i class="box"></i>DJ Pool Party</span><span class="check"><i class="box"></i>Golfing</span><span class="check"><i class="box"></i>Private Catamaran Booze Cruise</span><span class="check"><i class="box"></i>Private Deep-Sea Fishing</span><span class="check"><i class="box"></i>Private Chef</span><span class="check"><i class="box"></i>Transportation Services</span></div>
    <div class="checks" style="left:258px;top:276px"><span class="check"><i class="box"></i>Dune Buggies</span><span class="check"><i class="box"></i>Caribbean Beaches</span><span class="check"><i class="box"></i>Private Yacht Booze Cruise</span><span class="check"><i class="box"></i>Shared Catamaran Booze Cruise</span><span class="check"><i class="box"></i>All-Inclusive</span><span class="check"><i class="box"></i>Private Concierge</span></div>
    <div class="checks" style="left:413px;top:276px"><span class="check"><i class="box"></i>VIP Club Party</span><span class="check"><i class="box"></i>Nightlife Tour</span><span class="check"><i class="box"></i>Beach Dinner &amp; Party Warm-Up</span></div>
    <div class="checks" style="left:563px;top:276px;width:100px;gap:11px"><span class="check"><i class="box"></i>Strip and Gent's Clubs Tour</span><span class="check"><i class="box"></i>Casinos Tour</span><span class="check"><i class="box"></i>Beach Bar Crawl</span></div>

    <div class="label" style="left:110px;top:442px">Package Budget Per Person <b>*</b></div>
    <div class="label" style="left:258px;top:442px">First Name <b>*</b></div>
    <div class="label" style="left:368px;top:442px">Last Name <b>*</b></div>
    <div class="label" style="left:478px;top:442px">Email Address <b>*</b></div>
    <div class="field" style="left:110px;top:461px;width:135px">Ex: $500,600$ etc</div>
    <div class="field" style="left:258px;top:461px;width:97px"></div>
    <div class="field" style="left:368px;top:461px;width:97px"></div>
    <div class="field" style="left:478px;top:461px;width:97px"></div>
    <div class="label" style="left:110px;top:500px">Phone Number</div>
    <div class="label" style="left:258px;top:500px">Comments</div>
    <div class="field" style="left:110px;top:519px;width:135px"></div>
    <div class="field" style="left:258px;top:519px;width:207px"></div>
    <div class="send">SEND MY QUOTE</div>
  </form>

  <section class="activities">
    <h2 class="section-title">Bachelor Party<br>Mexico Night Time Activities</h2>
    <div class="activity" style="left:111px"><div class="activity-photo" role="img" aria-label="Photo of friends toasting in a garden" style="background:linear-gradient(135deg,#5a7a40,#b8a070)"></div><div class="activity-name">VIP Club Party</div></div>
    <div class="activity" style="left:249px"><div class="activity-photo" role="img" aria-label="Photo of friends laughing at a night party" style="background:linear-gradient(135deg,#3a2a22,#8a5a40)"></div><div class="activity-name">Nightlife Tour</div></div>
    <div class="activity" style="left:388px"><div class="activity-photo" role="img" aria-label="Photo of a dinner table set outdoors" style="background:linear-gradient(135deg,#4a6a30,#c8b890)"></div><div class="activity-name">Beach Dinner</div></div>
    <div class="activity" style="left:526px"><div class="activity-photo" role="img" aria-label="Photo of friends at an outdoor grill" style="background:linear-gradient(135deg,#8a8a80,#5a6a70)"></div><div class="activity-name">Beach Bar Crawl</div></div>
    <div class="dots"><i class="dot dot--on"></i><i class="dot"></i><i class="dot"></i></div>
  </section>

  <footer class="footer">
    <div class="brand"><div class="brand-ring"></div><div class="brand-name">Gold Harbor</div><div class="brand-sub">CONCIERGE</div></div>
    <div class="social"><i class="social-item" aria-label="Social link"></i><i class="social-item" aria-label="Social link"></i><i class="social-item" aria-label="Social link"></i><i class="social-item" aria-label="Social link"></i><i class="social-item" aria-label="Social link"></i><i class="social-item" aria-label="Social link"></i></div>
    <div class="rule"></div>
    <div class="copyright">Copyrights @ 2021 Gold Harbor Concierge.</div>
  </footer>
</section>

</body>
</html>
```